Your Joint Helper - Orthopedic needs from one site

We need slides that help to educate users, interest investors and allow the complexity of the entire continuum of care to be explained so anyone can understand. Your Joint Helper is a Varomin Health Company. Yourjointhelperhub.example. We allow people to evaluate, educate and engage with providers from one site. Simplyfying orthopedic care and wellness from one site. Patients, doctors, personal trainers, therapist, nutritionist, yoga, gyms, athletic trainers and more can connect from one site

Target Market(s)

Investors, Patients, Doctors and wellness providers

Industry/Entity Type

Healthcare

Requirements
Must have
• Investor slides, sales slides, education, process....

```html
<!DOCTYPE html>
<html lang="en">
<head>
<meta charset="utf-8">
<title>Your Joint Helper – Slides</title>
<link href="https://fonts.googleapis.com/css2?family=Poppins:wght@400;500;600;700;800&display=swap" rel="stylesheet">
<style>
:root{
  --navy:#0a2b6b;
  --navy-deep:#072257;
  --blue:#0e4aa0;
  --blue-mid:#0d3d8c;
  --green:#2fbf71;
  --green-light:#45d488;
  --teal:#27b39b;
  --white:#ffffff;
  --pink:#e23a7a;
  --cyan:#3bb5d6;
  --lime:#8cc63f;
  --orange:#f7941d;
  --purple:#7b4fa0;
  --muted:#cfe0ff;
}
*{box-sizing:border-box;margin:0;padding:0}
html,body{width:1200px;height:2768px;overflow:hidden;background:var(--white)}
body{position:relative;font-family:"Poppins",sans-serif;color:var(--white)}
.slide{position:absolute;left:96px;width:1016px;height:484px;overflow:hidden;
  background:radial-gradient(ellipse at 70% 40%,rgba(40,120,220,.45),transparent 60%),
  linear-gradient(135deg,#0a2f70 0%,#0e48a0 55%,#0a3580 100%)}
.abs{position:absolute}
.corner-tr{position:absolute;right:0;top:0}
.chevron-bl{position:absolute;left:0;bottom:0}
.side-rule{position:absolute;left:30px;top:0;width:1px;height:340px;background:rgba(255,255,255,.35)}
.top-arc{position:absolute;left:380px;top:-40px;width:520px;height:70px;border:1px solid rgba(120,170,255,.35);border-top:none;border-radius:0 0 40px 40px}
.slide-title{position:absolute;left:77px;top:34px;font-size:43px;font-weight:800;letter-spacing:.5px;
  background:linear-gradient(90deg,var(--green-light),var(--teal));-webkit-background-clip:text;background-clip:text;color:transparent}
.title-rule{position:absolute;left:77px;top:92px;width:122px;height:4px;background:var(--white)}
.footer{position:absolute;left:0;top:434px;width:100%;height:50px;background:rgba(5,25,80,.35)}
.footer-line{position:absolute;left:64px;top:0;right:0;height:1px;background:rgba(255,255,255,.7)}
.footer-dot{position:absolute;left:59px;top:-4px;width:9px;height:9px;border-radius:50%;background:var(--white)}
.footer-url{position:absolute;left:128px;top:11px;font-size:18px;font-weight:400}
.footer-globe{position:absolute;left:96px;top:14px;width:20px;height:20px}
.page-tab{position:absolute;right:0;top:8px;width:120px;height:42px;background:var(--navy-deep);border-radius:24px 0 0 0;
  font-size:18px;text-align:center;line-height:42px;padding-left:30px}
.icon-box{position:absolute;border:3px solid var(--green);border-radius:10px;background:var(--blue-mid);display:flex;align-items:center;justify-content:center}
.icon-box svg{width:60%;height:60%}
.small-text{font-size:9px;line-height:1.25;color:var(--muted)}
.caps-text{font-size:8.6px;line-height:1.3;text-transform:uppercase;color:var(--white);font-weight:500}

/* cover */
.cover-art{position:absolute;left:0;top:0;width:525px;height:484px;
  background:radial-gradient(circle at 48% 48%,#6fc4ff 0%,#1d72d8 22%,#0c3f97 48%,#0a2c70 80%)}
.logo-card{position:absolute;left:525px;top:0;width:366px;height:180px;background:var(--white);border-radius:0 0 40px 40px}
.logo-outline{position:absolute;left:533px;top:-10px;width:366px;height:196px;border:3px solid var(--green);border-top:none;border-left:none;border-radius:0 0 44px 44px}
.logo-mark{position:absolute;left:568px;top:62px;width:34px;height:34px;border-radius:50%;background:var(--green)}
.logo-name{position:absolute;left:616px;top:48px;font-size:27px;font-weight:700;line-height:1.15;color:var(--navy);letter-spacing:.5px}
.cover-copy{position:absolute;left:553px;top:298px;width:348px;font-size:17.5px;line-height:1.22;text-align:justify}

/* investor */
.pill{position:absolute;top:132px;width:42px;height:158px;background:linear-gradient(180deg,#35b561,#23964e);border-radius:6px;display:flex;align-items:center;justify-content:center}
.pill span{transform:rotate(-90deg);white-space:nowrap;font-size:17px}
.service{position:absolute;left:200px;font-size:17px}
.photo-frame{position:absolute;left:632px;top:82px;width:174px;height:152px;border:3px solid var(--green);border-radius:24px;
  background:linear-gradient(160deg,#e8eef4 0%,#b9c9d8 55%,#2b3442 100%)}
.clientele{position:absolute;left:640px;top:262px;width:160px;text-align:center;font-size:22px;font-weight:600}
.feature-title{position:absolute;font-size:22px;font-weight:600}
.feature-text{position:absolute;width:180px}

/* sales */
.kpi{position:absolute;top:124px;width:150px;text-align:center}
.kpi .icon-box{position:relative;margin:0 auto;width:52px;height:50px;border-width:2px;border-radius:6px}
.kpi-label{font-size:16px;margin-top:16px}
.kpi-value{font-size:24px;font-weight:600;margin-top:2px}
.kpi-note{font-size:9px;color:var(--muted);margin-top:0}
.block-title{position:absolute;font-size:22px;font-weight:600}
.block-note{position:absolute;font-size:9px;color:var(--muted)}
.pie{position:absolute;left:818px;top:170px;width:84px;height:84px;border-radius:50%;
  background:conic-gradient(var(--cyan) 0 36%,var(--lime) 36% 55%,var(--orange) 55% 74%,var(--pink) 74% 87%,var(--purple) 87% 94%,#2a5aa0 94% 100%)}
.legend{position:absolute;left:922px;top:176px;font-size:7px;line-height:12.6px}
.legend i{display:inline-block;width:7px;height:7px;margin-right:5px;vertical-align:-1px}
.bar{position:absolute;bottom:72px}
.axis-label{position:absolute;top:419px;font-size:9px;font-weight:600}
.product-list{position:absolute;font-size:12.5px;font-weight:600;line-height:18px}
.product-list i{display:inline-block;width:11px;height:9px;margin-right:12px}
.hbar{position:absolute;left:471px;height:9px}

/* education */
.edu-title{position:absolute;font-size:22px;font-weight:600}
.edu-text{position:absolute;width:160px}

/* process */
.step-label{position:absolute;top:224px;width:160px;text-align:center;font-size:22px;font-weight:600}
.step-line{position:absolute;top:165px;height:1px;background:rgba(255,255,255,.5)}
.dash{position:absolute;width:0;border-left:1px dashed rgba(255,255,255,.7)}
.dot{position:absolute;width:6px;height:6px;border-radius:50%;background:var(--white)}
.step-text{position:absolute;width:180px}
.workflow{position:absolute;left:814px;top:380px;font-size:24px;font-weight:600}
</style>
</head>
<body>

<svg width="0" height="0" style="position:absolute" aria-hidden="true">
  <defs>
    <symbol id="ico-people" viewBox="0 0 48 48"><g fill="#fff"><circle cx="24" cy="15" r="6"/><circle cx="11" cy="18" r="4.5"/><circle cx="37" cy="18" r="4.5"/><path d="M15 36c0-6 4-10 9-10s9 4 9 10z"/><path d="M3 35c0-5 3-8 8-8 2 0 3 .5 4 1-1.5 2-2 4-2 7z"/><path d="M45 35c0-5-3-8-8-8-2 0-3 .5-4 1 1.5 2 2 4 2 7z"/></g></symbol>
    <symbol id="ico-presenter" viewBox="0 0 48 48"><g fill="#fff"><rect x="22" y="6" width="20" height="13" rx="2"/><path d="M28 19l-3 5 7-5z"/><circle cx="14" cy="22" r="5"/><path d="M5 42v-8c0-4 3-6 7-6h6l8-6 2 3-9 8v9z"/><rect x="5" y="42" width="18" height="2"/></g><g fill="#0d3d8c"><circle cx="27" cy="12.5" r="1.5"/><circle cx="32" cy="12.5" r="1.5"/><circle cx="37" cy="12.5" r="1.5"/></g></symbol>
    <symbol id="ico-target" viewBox="0 0 48 48"><g fill="none" stroke="#fff" stroke-width="3.5"><circle cx="22" cy="26" r="17"/><circle cx="22" cy="26" r="10"/><path d="M22 26L38 10"/></g><circle cx="22" cy="26" r="3.5" fill="#fff"/><path d="M36 6l6 0-1 6-6 1z" fill="#fff"/></symbol>
    <symbol id="ico-eye" viewBox="0 0 48 48"><path d="M2 24C8 14 16 10 24 10s16 4 22 14c-6 10-14 14-22 14S8 34 2 24z" fill="#fff"/><circle cx="24" cy="24" r="8" fill="#0d3d8c"/><circle cx="24" cy="24" r="4" fill="#fff"/></symbol>
    <symbol id="ico-growth" viewBox="0 0 48 48"><g fill="#fff"><rect x="4" y="30" width="6" height="14"/><rect x="13" y="22" width="6" height="22"/><rect x="22" y="26" width="6" height="18"/><path d="M14 4l8 8h-5v8h-6v-8H6z"/></g><circle cx="35" cy="32" r="10" fill="none" stroke="#fff" stroke-width="3"/><text x="35" y="37" font-size="13" font-weight="700" text-anchor="middle" fill="#fff" font-family="Poppins,sans-serif">$</text></symbol>
    <symbol id="ico-warning" viewBox="0 0 48 48"><path d="M24 5L45 42H3z" fill="none" stroke="#fff" stroke-width="3" stroke-linejoin="round"/><rect x="22.5" y="17" width="3" height="14" fill="#fff"/><rect x="22.5" y="34" width="3" height="3" fill="#fff"/></symbol>
    <symbol id="ico-scope" viewBox="0 0 48 48"><g fill="none" stroke="#fff" stroke-width="4"><circle cx="24" cy="24" r="17"/><path d="M24 2v10M24 36v10M2 24h10M36 24h10"/></g><circle cx="24" cy="24" r="3" fill="#fff"/></symbol>
    <symbol id="ico-analysis" viewBox="0 0 48 48"><g fill="none" stroke="#fff" stroke-width="3.5" stroke-linecap="round"><circle cx="20" cy="20" r="15"/><path d="M31 31l12 12"/><path d="M10 24l6-7 5 5 8-9"/></g></symbol>
    <symbol id="ico-plan" viewBox="0 0 48 48"><g fill="none" stroke="#fff" stroke-width="3"><rect x="4" y="8" width="36" height="36" rx="2"/></g><path d="M14 36l4-10 22-22 6 6-22 22z" fill="#fff"/><path d="M14 36l10-4-6-6z" fill="#0d3d8c"/></symbol>
    <symbol id="ico-check" viewBox="0 0 48 48"><path d="M5 25l12 12L43 11" fill="none" stroke="#fff" stroke-width="8" stroke-linecap="round" stroke-linejoin="round"/></symbol>
    <symbol id="ico-globe" viewBox="0 0 24 24"><g fill="none" stroke="#fff" stroke-width="1.8"><circle cx="12" cy="12" r="10"/><ellipse cx="12" cy="12" rx="4.5" ry="10"/><path d="M2 12h20M4 6.5h16M4 17.5h16"/></g></symbol>
    <symbol id="shape-corner" viewBox="0 0 60 50"><path d="M10 0h50v50z" fill="#2fbf71"/><path d="M0 0h14l36 50H36z" fill="#27b39b" opacity=".7"/></symbol>
    <symbol id="shape-chevron" viewBox="0 0 70 140"><path d="M0 0l40 70L0 140z" fill="#27b39b"/><path d="M20 60l35 40-35 40H0l20-40z" fill="#2fbf71" opacity=".85"/></symbol>
  </defs>
</svg>

<!-- Cover -->
<section class="slide cover" style="top:75px">
  <div class="cover-art" role="img" aria-label="Illustration of a glowing digital human figure inside a futuristic circular interface"></div>
  <div class="logo-outline"></div>
  <div class="logo-card"></div>
  <div class="logo-mark"></div>
  <div class="logo-name">YOUR JOINT<br>HELPER</div>
  <p class="cover-copy">Lorem Ipsum has been the industry's standard dummy text ever since the 1500s, when an unknown printer</p>
  <svg class="abs" style="right:0;top:360px" width="80" height="124" viewBox="0 0 80 124" aria-hidden="true"><path d="M80 0v124H8z" fill="#27b39b" opacity=".55"/><path d="M80 50v74H40z" fill="#2fbf71"/></svg>
</section>

<!-- Investor -->
<section class="slide investor" style="top:604px">
  <div class="side-rule"></div><div class="top-arc"></div>
  <svg class="corner-tr" width="60" height="50" aria-hidden="true"><use href="#shape-corner"/></svg>
  <svg class="chevron-bl" width="70" height="140" aria-hidden="true"><use href="#shape-chevron"/></svg>
  <h2 class="slide-title">INVESTOR</h2><div class="title-rule"></div>

  <div class="pill" style="left:77px"><span>Service Area</span></div>
  <svg class="abs" style="left:118px;top:140px" width="90" height="140" aria-hidden="true">
    <g fill="none" stroke="#fff" stroke-width="1.2">
      <path d="M5 52L28 13H74"/><path d="M5 58L28 51H74"/><path d="M5 82L28 92H74"/><path d="M5 88L28 131H74"/>
    </g>
    <g fill="#fff"><circle cx="77" cy="13" r="4"/><circle cx="77" cy="51" r="4"/><circle cx="77" cy="92" r="4"/><circle cx="77" cy="131" r="4"/></g>
  </svg>
  <div class="service" style="top:140px">Service 1</div>
  <div class="service" style="top:178px">Service 2</div>
  <div class="service" style="top:219px">Service 3</div>
  <div class="service" style="top:258px">Service 4</div>
  <div class="pill" style="left:301px"><span>Offering</span></div>

  <div class="icon-box" style="left:478px;top:62px;width:85px;height:78px"><svg><use href="#ico-people"/></svg></div>
  <div class="icon-box" style="left:478px;top:198px;width:85px;height:78px"><svg><use href="#ico-people"/></svg></div>
  <div class="icon-box" style="left:862px;top:62px;width:85px;height:78px"><svg><use href="#ico-people"/></svg></div>
  <div class="icon-box" style="left:862px;top:198px;width:85px;height:78px"><svg><use href="#ico-people"/></svg></div>
  <svg class="abs" style="left:563px;top:90px" width="300" height="160" aria-hidden="true">
    <g fill="none" stroke="#2fbf71" stroke-width="1.2"><path d="M10 8h32l12 12"/><path d="M10 150h32l12-12"/><path d="M290 8h-32l-12 12"/><path d="M290 150h-32l-12-12"/></g>
  </svg>
  <div class="photo-frame" role="img" aria-label="Photo of a doctor shaking hands with a businessman, medical staff in the background"></div>
  <div class="clientele">Clientele</div>

  <div class="icon-box" style="left:78px;top:340px;width:71px;height:67px"><svg><use href="#ico-presenter"/></svg></div>
  <div class="feature-title" style="left:162px;top:340px">Introduction</div>
  <p class="feature-text small-text" style="left:162px;top:375px">Lorem ipsum dolor sit amet, consectetur adipiscing elit, sed do eiusmod tempor incididunt ut labore et</p>
  <div class="icon-box" style="left:394px;top:340px;width:71px;height:67px"><svg><use href="#ico-target"/></svg></div>
  <div class="feature-title" style="left:480px;top:340px">Mission</div>
  <p class="feature-text small-text" style="left:480px;top:375px">Lorem ipsum dolor sit amet, consectetur adipiscing elit, sed do eiusmod tempor incididunt ut labore et</p>
  <div class="icon-box" style="left:700px;top:340px;width:71px;height:67px"><svg><use href="#ico-eye"/></svg></div>
  <div class="feature-title" style="left:786px;top:340px">Vision</div>
  <p class="feature-text small-text" style="left:786px;top:375px">Lorem ipsum dolor sit amet, consectetur adipiscing elit, sed do eiusmod tempor incididunt ut labore et</p>

  <footer class="footer"><div class="footer-line"></div><div class="footer-dot"></div>
    <svg class="footer-globe"><use href="#ico-globe"/></svg><span class="footer-url">Yourjointhelperhub.example</span>
    <div class="page-tab">1</div></footer>
</section>

<!-- Sales -->
<section class="slide sales" style="top:1131px">
  <div class="side-rule"></div><div class="top-arc"></div>
  <svg class="corner-tr" width="60" height="50" aria-hidden="true"><use href="#shape-corner"/></svg>
  <svg class="chevron-bl" width="70" height="140" aria-hidden="true"><use href="#shape-chevron"/></svg>
  <h2 class="slide-title">SALES</h2><div class="title-rule"></div>

  <div class="kpi" style="left:66px"><div class="icon-box"><svg><use href="#ico-presenter"/></svg></div><div class="kpi-label">SALES</div><div class="kpi-value">956,381</div><div class="kpi-note">Lorem ipsum dolor sit amet,</div></div>
  <div class="kpi" style="left:238px"><div class="icon-box"><svg><use href="#ico-growth"/></svg></div><div class="kpi-label">PROFIT</div><div class="kpi-value">956,381</div><div class="kpi-note">Lorem ipsum dolor sit amet,</div></div>
  <div class="kpi" style="left:425px"><div class="icon-box"><svg><use href="#ico-people"/></svg></div><div class="kpi-label">CUSTOMERS</div><div class="kpi-value">956,381</div><div class="kpi-note">Lorem ipsum dolor sit amet,</div></div>
  <div class="kpi" style="left:610px"><div class="icon-box"><svg><use href="#ico-warning"/></svg></div><div class="kpi-label">RISKS</div><div class="kpi-value">956,381</div><div class="kpi-note">Lorem ipsum dolor sit amet,</div></div>

  <div class="block-title" style="left:818px;top:112px;font-size:20px">Top Categories</div>
  <div class="block-note" style="left:818px;top:145px">Lorem ipsum dolor sit amet,</div>
  <div class="pie" role="img" aria-label="Pie chart of top categories"></div>
  <div class="legend">
    <div><i style="background:var(--cyan)"></i>2.6 %</div><div><i style="background:var(--purple)"></i>2.6 %</div><div><i style="background:var(--pink)"></i>2.6 %</div>
    <div><i style="background:var(--orange)"></i>2.6 %</div><div><i style="background:var(--lime)"></i>2.6 %</div><div><i style="background:#2a5aa0"></i>2.6 %</div>
  </div>

  <div class="block-title" style="left:77px;top:296px">Sales Analysis</div>
  <div class="block-note" style="left:77px;top:330px">Lorem ipsum dolor sit amet,</div>
  <div class="bar" style="left:83px;width:12px;height:36px;background:var(--cyan)"></div>
  <div class="bar" style="left:98px;width:12px;height:52px;background:var(--lime)"></div>
  <div class="bar" style="left:137px;width:12px;height:18px;background:var(--cyan)"></div>
  <div class="bar" style="left:152px;width:12px;height:40px;background:var(--lime)"></div>
  <div class="bar" style="left:193px;width:12px;height:44px;background:var(--cyan)"></div>
  <div class="bar" style="left:208px;width:12px;height:30px;background:var(--lime)"></div>
  <div class="bar" style="left:250px;width:12px;height:30px;background:var(--cyan)"></div>
  <div class="bar" style="left:265px;width:12px;height:68px;background:var(--lime)"></div>
  <div class="axis-label" style="left:88px">2010</div><div class="axis-label" style="left:142px">2015</div>
  <div class="axis-label" style="left:198px">2018</div><div class="axis-label" style="left:255px">2021</div>

  <div class="block-title" style="left:369px;top:296px">Sales Products</div>
  <div class="block-note" style="left:369px;top:330px">Lorem ipsum dolor sit amet,</div>
  <div class="product-list" style="left:369px;top:349px">
    <div><i style="background:var(--pink)"></i>Product A</div><div><i style="background:var(--cyan)"></i>Product B</div>
    <div><i style="background:var(--lime)"></i>Product C</div><div><i style="background:var(--orange)"></i>Product D</div>
  </div>
  <div class="hbar" style="top:354px;width:196px;background:var(--pink)"></div>
  <div class="hbar" style="top:372px;width:246px;background:var(--cyan)"></div>
  <div class="hbar" style="top:390px;width:143px;background:var(--lime)"></div>
  <div class="hbar" style="top:408px;width:62px;background:var(--orange)"></div>

  <div class="block-title" style="left:789px;top:296px">Sales Budget</div>
  <div class="block-note" style="left:789px;top:330px">Lorem ipsum dolor sit amet,</div>
  <div class="product-list" style="left:789px;top:349px">
    <div><i style="background:var(--pink)"></i>Product A</div><div><i style="background:var(--cyan)"></i>Product B</div>
    <div><i style="background:var(--lime)"></i>Product C</div><div><i style="background:var(--orange)"></i>Product D</div>
  </div>
  <div class="bar" style="left:897px;width:9px;height:52px;background:var(--pink)"></div>
  <div class="bar" style="left:912px;width:9px;height:66px;background:var(--cyan)"></div>
  <div class="bar" style="left:927px;width:9px;height:38px;background:var(--lime)"></div>
  <div class="bar" style="left:942px;width:9px;height:16px;background:var(--orange)"></div>

  <footer class="footer"><div class="footer-line"></div><div class="footer-dot"></div>
    <svg class="footer-globe"><use href="#ico-globe"/></svg><span class="footer-url">Yourjointhelperhub.example</span>
    <div class="page-tab">2</div></footer>
</section>

<!-- Education -->
<section class="slide education" style="top:1667px">
  <div class="side-rule"></div><div class="top-arc"></div>
  <svg class="corner-tr" width="60" height="50" aria-hidden="true"><use href="#shape-corner"/></svg>
  <svg class="chevron-bl" width="70" height="140" aria-hidden="true"><use href="#shape-chevron"/></svg>
  <h2 class="slide-title">EDUCATION</h2><div class="title-rule"></div>

  <div class="icon-box" style="left:77px;top:153px;width:79px;height:74px"><svg><use href="#ico-presenter"/></svg></div>
  <div class="edu-title" style="left:176px;top:156px">Arthroplasty</div>
  <p class="edu-text caps-text" style="left:178px;top:188px">Lorem ipsum dolor sit amet, consectetur adipiscing elit, sed do eiusmod tempor incididunt ut labore et dolore</p>
  <div class="icon-box" style="left:386px;top:153px;width:79px;height:74px"><svg><use href="#ico-presenter"/></svg></div>
  <div class="edu-title" style="left:486px;top:156px">Osteoporosis</div>
  <p class="edu-text caps-text" style="left:488px;top:188px">Lorem ipsum dolor sit amet, consectetur adipiscing elit, sed do eiusmod tempor incididunt ut labore et dolore</p>
  <div class="icon-box" style="left:693px;top:153px;width:79px;height:74px"><svg><use href="#ico-presenter"/></svg></div>
  <div class="edu-title" style="left:792px;top:156px">Spinal Disorders</div>
  <p class="edu-text caps-text" style="left:794px;top:188px">Lorem ipsum dolor sit amet, consectetur adipiscing elit, sed do eiusmod tempor incididunt ut labore et dolore</p>

  <div class="icon-box" style="left:77px;top:292px;width:79px;height:74px"><svg><use href="#ico-presenter"/></svg></div>
  <div class="edu-title" style="left:176px;top:295px">Joint Disorders</div>
  <p class="edu-text caps-text" style="left:178px;top:328px">Lorem ipsum dolor sit amet, consectetur adipiscing elit, sed do eiusmod tempor incididunt ut labore et dolore</p>
  <div class="icon-box" style="left:388px;top:292px;width:79px;height:74px"><svg><use href="#ico-presenter"/></svg></div>
  <div class="edu-title" style="left:488px;top:295px">Ankle Fractures</div>
  <p class="edu-text caps-text" style="left:490px;top:328px">Lorem ipsum dolor sit amet, consectetur adipiscing elit, sed do eiusmod tempor incididunt ut labore et dolore</p>
  <div class="icon-box" style="left:695px;top:292px;width:79px;height:74px"><svg><use href="#ico-presenter"/></svg></div>
  <div class="edu-title" style="left:795px;top:295px">ACL Tear</div>
  <p class="edu-text caps-text" style="left:797px;top:328px">Lorem ipsum dolor sit amet, consectetur adipiscing elit, sed do eiusmod tempor incididunt ut labore et dolore</p>

  <footer class="footer"><div class="footer-line"></div><div class="footer-dot"></div>
    <svg class="footer-globe"><use href="#ico-globe"/></svg><span class="footer-url">Yourjointhelperhub.example</span>
    <div class="page-tab">3</div></footer>
</section>

<!-- Process -->
<section class="slide process" style="top:2203px">
  <div class="side-rule"></div><div class="top-arc"></div>
  <svg class="corner-tr" width="60" height="50" aria-hidden="true"><use href="#shape-corner"/></svg>
  <svg class="chevron-bl" width="70" height="140" aria-hidden="true"><use href="#shape-chevron"/></svg>
  <h2 class="slide-title">PROCESSS</h2><div class="title-rule"></div>

  <div class="icon-box" style="left:130px;top:126px;width:78px;height:76px"><svg><use href="#ico-scope"/></svg></div>
  <div class="icon-box" style="left:365px;top:126px;width:78px;height:76px"><svg><use href="#ico-analysis"/></svg></div>
  <div class="icon-box" style="left:595px;top:126px;width:78px;height:76px"><svg><use href="#ico-plan"/></svg></div>
  <div class="icon-box" style="left:816px;top:126px;width:78px;height:76px"><svg><use href="#ico-check"/></svg></div>
  <div class="step-line" style="left:236px;width:102px"></div>
  <div class="step-line" style="left:470px;width:105px"></div>
  <div class="step-line" style="left:698px;width:100px"></div>
  <div class="step-label" style="left:89px">Scope</div>
  <div class="step-label" style="left:324px">Analysis</div>
  <div class="step-label" style="left:554px">Plan</div>
  <div class="step-label" style="left:775px">Done</div>

  <div class="dash" style="left:169px;top:262px;height:80px"></div><div class="dot" style="left:166px;top:341px"></div>
  <div class="dash" style="left:404px;top:262px;height:54px"></div><div class="dot" style="left:401px;top:315px"></div>
  <div class="dash" style="left:634px;top:262px;height:36px"></div><div class="dot" style="left:631px;top:297px"></div>
  <div class="dash" style="left:855px;top:262px;height:12px"></div><div class="dot" style="left:852px;top:273px"></div>

  <p class="step-text caps-text" style="left:103px;top:355px">Lorem ipsum dolor sit amet, consectetur adipiscing elit, sed do eiusmod tempor</p>
  <p class="step-text caps-text" style="left:338px;top:330px">Lorem ipsum dolor sit amet, consectetur adipiscing elit, sed do eiusmod tempor</p>
  <p class="step-text caps-text" style="left:567px;top:311px">Lorem ipsum dolor sit amet, consectetur adipiscing elit, sed do eiusmod tempor</p>
  <p class="step-text caps-text" style="left:788px;top:290px">Lorem ipsum dolor sit amet, consectetur adipiscing elit, sed do eiusmod tempor</p>
  <svg class="abs" style="left:0;top:0" width="1016" height="440" aria-hidden="true">
    <path d="M88 414V385H322V360H548V339H765V318H982" fill="none" stroke="#fff" stroke-width="1.2"/>
  </svg>
  <div class="workflow">Work Flow</div>

  <footer class="footer"><div class="footer-line"></div><div class="footer-dot"></div>
    <svg class="footer-globe"><use href="#ico-globe"/></svg><span class="footer-url">Yourjointhelperhub.example</span>
    <div class="page-tab">4</div></footer>
</section>

</body>
</html>
```